A WEBSITE FOR A JEWELLERY RETAIL STORE WITH A SHOPPING CART, AND ABILITY TO ORDER ONLINE.

I require a website with a shopping cart.

We sell MAINLY diamond jewellery (such as rings etc). I need it to be simple to change prices with only a few buttons, as the price fluctuates due to the US Dollar.

We are a diamond wholesaler, selling directly to the public, so we guarantee the lowest prices in Australia.

There is also a link to current inventory that will need to be uploaded to the site.

This could be an ongoing job, where you will be paid weekly to maintain and update the website if you wish.

Target Market(s)

People getting engaged, and wanting to buy a diamond ring.

Number of Pages Required

5+ page

Colors

Designer to choose colors to be used in the design.

Requirements
Must have
• elegant.
• modern.
• professional.
• SHOPPING CART.
• ABILITY TO SEARCH FOR LOOSE DIAMONDS (LINK THAT NEEDS TO BE EMBEDDED WILL BE SENT WHICH SHOWS CURRENT STOCK).
• ENGAGEMENT RINGS
• WEDDING RINGS
• DIAMOND EARRINGS
• DIAMOND PENDANTS
• LOOSE DIAMONDS.
• SALE ITEMS.
• OTHER JEWELLERY.
• EDUCATION
• WISH LIST
• CART.
Nice to have
• a good place to look for inspiration on pages is https://www.lumenvael.example.
• YOU MAY VISIT OUR FACEBOOK PAGE AT.
• HTTP://WWW.SOCIALPAGE.EXAMPLE/QUILLSTONEJEWELLERS
Should not have
• We don't want it too busy.

```html
<!DOCTYPE html>
<html lang="en">
<head>
<meta charset="utf-8">
<title>Quillstone Jewellers</title>
<link rel="stylesheet" href="https://fonts.googleapis.com/css2?family=Playfair+Display:wght@600&family=Roboto:wght@300&family=Hind:wght@400;500&family=Josefin+Sans:wght@300&display=swap">
<style>
  :root {
    --backdrop: #7d5a48;
    --bar: #1c1a19;
    --nav: rgba(22, 20, 19, 0.78);
    --gold: #c9953c;
    --gold-bright: #f2c35a;
    --white: #ffffff;
    --panel: rgba(70, 58, 50, 0.88);
  }
  * { margin: 0; padding: 0; box-sizing: border-box; }
  html, body { width: 1200px; height: 952px; overflow: hidden; background: var(--backdrop); }

  .site {
    position: absolute; left: 0; top: 101px;
    width: 1200px; height: 750px; overflow: hidden;
    font-family: "Hind", sans-serif;
  }
  .hero-photo {
    position: absolute; inset: 0;
    background:
      radial-gradient(ellipse 40% 55% at 78% 55%, rgba(200,150,120,0.75), rgba(0,0,0,0) 70%),
      radial-gradient(ellipse 30% 30% at 20% 30%, rgba(150,130,115,0.6), rgba(0,0,0,0) 70%),
      linear-gradient(135deg, #4a3d36 0%, #6e5a4e 40%, #8a6650 65%, #5a4336 100%);
  }
  .hero-shade { position: absolute; inset: 0; background: rgba(30, 22, 18, 0.25); }

  .top-bar {
    position: absolute; left: 0; top: 0; width: 100%; height: 45px;
    background: var(--bar);
  }
  .phone {
    position: absolute; left: 98px; top: 10px;
    display: flex; align-items: center; gap: 12px;
    color: var(--gold); font-size: 19px; letter-spacing: 0.5px;
  }
  .account-links {
    position: absolute; left: 859px; top: 11px;
    display: flex; gap: 26px;
    color: var(--gold); font-size: 19px; font-weight: 500; letter-spacing: 0.6px;
  }
  .flag { position: absolute; left: 1055px; top: 10px; }

  .main-nav {
    position: absolute; left: 0; top: 45px; width: 100%; height: 101px;
    background: var(--nav);
  }
  .brand { position: absolute; left: 98px; top: 22px; display: flex; align-items: center; gap: 12px; }
  .brand-mark { width: 46px; height: 46px; background: var(--white); }
  .brand-name {
    color: var(--white); font-family: "Josefin Sans", sans-serif; font-weight: 300;
    line-height: 1;
  }
  .brand-name .line1 { display: block; font-size: 38px; letter-spacing: 0.5px; }
  .brand-name .line2 { display: block; font-size: 16px; letter-spacing: 12.5px; margin-top: 6px; }

  .menu { position: absolute; top: 34px; left: 553px; display: flex; gap: 24px; list-style: none; }
  .menu li { color: var(--gold-bright); font-size: 20px; display: flex; align-items: center; gap: 3px; }

  .hero-copy { position: absolute; left: 0; top: 345px; width: 100%; text-align: center; color: var(--white); }
  .hero-title { font-family: "Playfair Display", serif; font-weight: 600; font-size: 68px; line-height: 1; }
  .hero-sub {
    font-family: "Roboto", sans-serif; font-weight: 300; font-size: 32px;
    letter-spacing: 1px; margin-top: 28px;
  }

  .cta {
    position: absolute; top: 548px; width: 220px; height: 72px;
    border: 2px solid var(--gold-bright); color: var(--white);
    display: flex; align-items: center; justify-content: center;
    font-size: 18px; font-weight: 500; letter-spacing: 0.4px;
  }
  .cta-rings { left: 347px; }
  .cta-diamonds { left: 622px; }

  .side-tab {
    position: absolute; left: 1133px; width: 67px; height: 75px;
    background: var(--panel); display: flex; align-items: center; justify-content: center;
  }
  .tab-wishlist { top: 340px; }
  .tab-cart { top: 444px; }

  .search-panel {
    position: absolute; left: 929px; top: 548px; width: 271px; height: 76px;
    background: var(--panel);
  }
  .search-field {
    position: absolute; left: 28px; top: 14px; width: 207px; height: 48px;
    border: 2px solid var(--gold-bright); border-radius: 24px;
    color: #b9a89a; font-size: 18px; padding: 13px 0 0 18px;
  }
</style>
</head>
<body>
  <div class="site">
    <div class="hero-photo" role="img" aria-label="Close-up photograph of a hand wearing a diamond engagement ring"></div>
    <div class="hero-shade"></div>

    <header class="top-bar">
      <div class="phone">
        <svg width="22" height="22" viewBox="0 0 24 24" aria-hidden="true"><path fill="#c9953c" d="M6.6 10.8c1.4 2.8 3.8 5.1 6.6 6.6l2.2-2.2c.3-.3.7-.4 1-.2 1.1.4 2.3.6 3.6.6.6 0 1 .4 1 1V20c0 .6-.4 1-1 1C10.6 21 3 13.4 3 4c0-.6.4-1 1-1h3.5c.6 0 1 .4 1 1 0 1.3.2 2.5.6 3.6.1.3 0 .7-.2 1z"/></svg>
        <span>(555) 014-2870</span>
      </div>
      <nav class="account-links"><span>LOGIN</span><span>SIGN UP</span></nav>
      <svg class="flag" width="34" height="22" viewBox="0 0 34 22" aria-label="Region: United States">
        <rect width="34" height="22" fill="#fff"/>
        <g fill="#c8313e">
          <rect y="0" width="34" height="2"/><rect y="4" width="34" height="2"/><rect y="8" width="34" height="2"/>
          <rect y="12" width="34" height="2"/><rect y="16" width="34" height="2"/><rect y="20" width="34" height="2"/>
        </g>
        <rect width="15" height="12" fill="#3c3b7e"/>
      </svg>
    </header>

    <div class="main-nav">
      <div class="brand">
        <span class="brand-mark"></span>
        <span class="brand-name"><span class="line1">QUILLSTONE</span><span class="line2">JEWELLERS</span></span>
      </div>
      <ul class="menu">
        <li>Diamonds<svg width="14" height="10" viewBox="0 0 14 10"><path d="M1 2l6 6 6-6" fill="none" stroke="#f2c35a" stroke-width="1.4"/></svg></li>
        <li>Rings<svg width="14" height="10" viewBox="0 0 14 10"><path d="M1 2l6 6 6-6" fill="none" stroke="#f2c35a" stroke-width="1.4"/></svg></li>
        <li>Earrings<svg width="14" height="10" viewBox="0 0 14 10"><path d="M1 2l6 6 6-6" fill="none" stroke="#f2c35a" stroke-width="1.4"/></svg></li>
        <li>Others<svg width="14" height="10" viewBox="0 0 14 10"><path d="M1 2l6 6 6-6" fill="none" stroke="#f2c35a" stroke-width="1.4"/></svg></li>
        <li>Eductation</li>
      </ul>
    </div>

    <section class="hero-copy">
      <h1 class="hero-title">You Design It we Build It</h1>
      <p class="hero-sub">Create your own unique diamond engagement ring.</p>
    </section>

    <a class="cta cta-rings">Engagement Rings</a>
    <a class="cta cta-diamonds">Loose Diamonds</a>

    <div class="side-tab tab-wishlist" aria-label="Wish list">
      <svg width="40" height="36" viewBox="0 0 40 36"><path d="M20 33S3 22 3 11.5C3 6.5 7 3 11.5 3c3.6 0 6.6 2.2 8.5 5 1.9-2.8 4.9-5 8.5-5C33 3 37 6.5 37 11.5 37 22 20 33 20 33z" fill="none" stroke="#f2c35a" stroke-width="2.4" stroke-linejoin="round"/></svg>
    </div>
    <div class="side-tab tab-cart" aria-label="Cart">
      <svg width="46" height="42" viewBox="0 0 46 42"><path d="M2 4h6l5 22h24l5-16H11" fill="none" stroke="#f2c35a" stroke-width="2.4" stroke-linejoin="round" stroke-linecap="round"/><circle cx="17" cy="35" r="3" fill="none" stroke="#f2c35a" stroke-width="2.2"/><circle cx="33" cy="35" r="3" fill="none" stroke="#f2c35a" stroke-width="2.2"/></svg>
    </div>

    <div class="search-panel">
      <div class="search-field">search</div>
    </div>
  </div>
</body>
</html>
```